Kestrel Aeronautics website

We are an aviation company based in Miramar, FL but with worldwide coverage. We are involved in commercial aircraft (mostly freighters) trading, sale & leasing. Specifically, we specialized in freighters of the Valdane family (V412, V418, V424, V436, V448). We also assist with financing, sale/leaseback. Handle special aviation projects and provide consultancy services. Currently engaged in a Valdane 777 passenger to Freighter conversion (P2F).

Website Preliminary Initial Content/Sections as follows:

About Us
Founded in 2011, Kestrel Aeronautics' management has many years of experience in Aviation, a strong background in scheduled airlines with emphasis in all cargo operations, freight forwarding supply chain and freight logistics, as well as ACMI and CMI operations.

Kestrel’s focuses in facilitating wet and dry lease operations, charter and ACMI programs consultancy, aircraft sales, leasing and procurement, aviation consultancy and aircraft management.

Kestrel team is a hands-on reliable alternative that works toward achieving your aircraft and aviation objectives by meeting your requirements and timeframe throughout professional and personalized service.

Tiberio Salcedo has over three decades of experience in the aviation field including aircraft maintenance, airline management, supply chain and logistics management. Tiberio is a true entrepreneur with proven experience and expertise on the multiple facets of the commercial aviation industry throughout the creation and development of a cluster of aviation entities. Tiberio is the founder and former sole member/chairman of 64 Sky, a Valdane 767 All-Cargo U.S. Certificated Air Carrier created from scratch in 2014 which nowadays conforms a superb growing airline platform with an immaculate compliance operational record.

Services

Aircraft Finance, Trading, Procurement and Leasing
Kestrel buys, sells, leases and facilitates aircraft trading while specializes in structured aircraft investment projects. Kestrel has deep industry relationships and years of expertise, allowing to successfully execute lease transactions. We assist airlines, financial institutions and leasing companies when selling or purchasing aircraft.

Aircraft Available for Sale/Lease

Sale/Leaseback
Sale-leaseback is a method of financing. If your company needs liquidity, your aircraft or engine can serve as collateral for a loan throughout a sale-leaseback transaction. Sale-leaseback can free the equity tied up in aircraft or asset. Even if there is no pressing need for funds, a sale-leaseback allows you to use the equity tied up in your aircraft in a more productive fashion. Leaseback arrangements are usually employed because they confer financing, accounting or taxation benefits.

Passenger to Freighter Conversion (P2F)
Pandemic has seen the resurgence of operators packing freight into the main cabins of passenger aircraft. Carriers have been allowed to transport cargo in the cabin by removing passenger seats completely. FAA/EASA have established exemptions that allow operators to fly in “Preighter” configuration for a limited time. Kestrel is closely working with a U.S. group that is developing a Class E Supplemental Type Certificate (STC) for applicability on V448 aircraft which will include a cargo door for containerized freight. Final approvals are expected during first quarter of 2022.
Wet lease
Throughout our deep relationships within the industry, Kestrel facilitates short or long-term wet leases to airlines and qualified parties around the globe, whereby we provide the Aircraft, Crews, Maintenance and Insurance (ACMI) worldwide services at competitive rates. We also specialize in AM leases where the aircraft is registered onto Lessee´s AOC with all maintenance services included in the rates, covering all maintenance risks, or CM or CMI where the client provides the aircraft.

Dry Lease
We offer aircraft from our own portfolio on dry lease or could engage in procuring the aircraft of your choice.

Asset & Aircraft Management
We provide aircraft owners Aircraft Management services, where we manage the technical side of the aircraft or the asset. Kestrel also provides Harlan Motive engines trading, repair and full management services. We also buy Valdane/Skyvane surplus inventory.

Worldwide Charters
We facilitate the arrangement of full charters to airlines and logistics companies. Certain territory restrictions may apply.

Aviation Consultancy
We provide airline consultancy services for new or special projects. Kestrel also specializes on All Cargo International route analysis, implementation and development. Our team provides professional guidance in obtaining worldwide both scheduled and charter authority.

Target Market(s)

Our target market are the airlines, logistics companies and commercial aviation related entities

Industry/Entity Type

Commercial Aviation

Coding

Coded - Design and coding required

Number of Pages Required

3 page

Requirements
Must have
• Illustrations of wide body freighters such V448, V436, V418

```html
<!DOCTYPE html>
<html lang="en">
<head>
<meta charset="utf-8">
<title>Kestrel Aeronautics</title>
<link rel="stylesheet" href="https://fonts.googleapis.com/css2?family=Cinzel:wght@700;900&family=Outfit:wght@400;500;600&display=swap">
<style>
  :root {
    --navy: #0b1a4a;
    --sky-top: #2f6fc6;
    --sky-mid: #4a8ad8;
    --cloud: #e9eef5;
    --cloud-white: #f7f9fc;
    --white: #ffffff;
    --ink: #111827;
    --accent: #e8552a;
  }
  * { margin: 0; padding: 0; box-sizing: border-box; }
  html, body { width: 1200px; height: 780px; overflow: hidden; background: var(--white); }
  .page { position: relative; width: 1200px; height: 780px; overflow: hidden; font-family: "Outfit", sans-serif; }
  .hero-photo {
    position: absolute; inset: 0;
    background:
      radial-gradient(ellipse 520px 260px at 980px 430px, rgba(236,241,248,0.95), rgba(236,241,248,0) 70%),
      radial-gradient(ellipse 700px 300px at 420px 640px, rgba(240,244,250,0.95), rgba(240,244,250,0) 70%),
      linear-gradient(180deg, var(--sky-top) 0%, var(--sky-mid) 38%, var(--cloud) 72%, var(--cloud-white) 100%);
  }
  .brand-box {
    position: absolute; left: 209px; top: 8px; width: 133px; height: 140px;
    background: var(--navy);
    display: flex; align-items: center; justify-content: center; text-align: center;
  }
  .brand-name {
    color: var(--white); font-family: "Outfit", sans-serif; font-weight: 400;
    font-size: 12px; letter-spacing: 1.5px; text-transform: uppercase; line-height: 1.4;
  }
  .main-nav { position: absolute; left: 633px; top: 63px; display: flex; gap: 14px; }
  .main-nav a {
    font-family: "Outfit", sans-serif; font-weight: 600; font-size: 14px;
    color: var(--white); text-decoration: none;
  }
  .main-nav a.is-current { color: var(--navy); }
  .hero-copy { position: absolute; left: 209px; top: 218px; }
  .hero-title {
    font-family: "Cinzel", serif; font-weight: 900; color: var(--navy);
    font-size: 66px; line-height: 0.98; letter-spacing: -1px;
  }
  .hero-text {
    margin-top: 20px; width: 420px;
    font-size: 17px; line-height: 1.35; color: var(--ink);
  }
  .btn-outline {
    display: inline-flex; align-items: center; justify-content: center;
    margin-top: 20px; width: 191px; height: 43px;
    border: 1.5px solid var(--accent); color: var(--accent);
    font-family: "Outfit", sans-serif; font-size: 18px; letter-spacing: 2px;
    text-decoration: none; text-transform: uppercase;
  }
</style>
</head>
<body>
  <div class="page">
    <div class="hero-photo" role="img" aria-label="Wide body freighter aircraft climbing over white clouds in a blue sky"></div>

    <header>
      <div class="brand-box"><span class="brand-name">Kestrel<br>Aeronautics</span></div>
      <nav class="main-nav">
        <a href="#" class="is-current">Home</a>
        <a href="#">About us</a>
        <a href="#">Services</a>
        <a href="#">Sale/Leaseback</a>
      </nav>
    </header>

    <section class="hero-copy">
      <h1 class="hero-title">Kestrel<br>Aeronautics'</h1>
      <p class="hero-text">We are an aviation company based in Miramar, FL but with worldwide coverage.</p>
      <a href="#" class="btn-outline">Learn more</a>
    </section>
  </div>
</body>
</html>
```